Bramblewood Coatings of Central Florida, LLC. Start-up painting business needs a professional web desig

We have a start up painting business that would like to reach/focus on commercial clients like building contractors, HOA's, apartment complexes, etc.. We would like a residential aspect to the web design as well. We have an existing website at "trybramblewoodcoats.com" with usable content. Have logo and color scheme attached. Use provided website ONLY as template. Add commercial services page. Can type own content when needed.

Industry/Entity Type

Apartment

Number of Pages Required

5+ page

Font styles to use
Serif
Sans Serif
Decorative
Script

Requirements
Must have
• Commercial services

```html
<!DOCTYPE html>
<html lang="en">
<head>
<meta charset="utf-8">
<title>Bramblewood Coatings of Central Florida, LLC</title>
<link href="https://fonts.googleapis.com/css2?family=Lato:wght@400;700&display=swap" rel="stylesheet">
<style>
:root{
  --salmon:#e39178;
  --olive:#6a6436;
  --ink:#2a2a2a;
  --muted:#555;
  --rule:#cfcfcf;
  --tile:#efefef;
  --footer:#2c2c2c;
  --white:#fff;
}
*{box-sizing:border-box;margin:0;padding:0}
html,body{width:974px;height:1200px;overflow:hidden;background:var(--white);font-family:'Lato',sans-serif;color:var(--ink)}
.page{position:relative;width:974px;height:1200px}
.abs{position:absolute}
.brand{left:114px;top:18px;display:flex;align-items:center;gap:14px}
.brand-mark{width:74px;height:70px;background:#e9dcd3;border-radius:6px}
.brand-name{color:var(--salmon);font-weight:700;font-size:21px;line-height:24px}
.social{left:601px;top:22px;display:flex;gap:8px}
.social span{width:24px;height:24px;border-radius:4px;background:#2d5d80}
.social span:last-child{background:#b43b2e}
.divider{left:727px;top:14px;width:1px;height:38px;background:#555}
.phone-icon{left:736px;top:22px}
.phones{left:766px;top:19px;font-size:13px;line-height:15px;font-weight:700;color:#333}
.nav{top:72px;right:114px;display:flex;gap:30px;font-size:13px;font-weight:700}
.nav a{color:var(--ink);text-decoration:none;padding-bottom:4px}
.nav a.active{color:var(--salmon);border-bottom:2px solid var(--salmon)}
.hero{left:0;top:105px;width:974px;height:381px;background:linear-gradient(90deg,#efe9e3 0%,#e8d4c4 40%,#5c84c4 62%,#e7e3df 82%,#8fb4dc 100%)}
.hero-title{left:114px;top:168px;width:240px;font-size:23px;line-height:34px;font-weight:700;color:#111}
.arrow{width:31px;height:31px;border-radius:50%;background:var(--white);border:1px solid #bbb;display:flex;align-items:center;justify-content:center}
.estimate{left:604px;top:436px;width:259px;height:172px;background:var(--white);box-shadow:0 0 10px rgba(0,0,0,.15);border-radius:6px 6px 0 0}
.estimate h2{position:absolute;left:14px;top:14px;font-size:18px;font-weight:700;color:#222;white-space:nowrap}
.field{position:absolute;left:622px;width:223px;height:26px;border:1px solid #ccc;border-radius:3px;background:var(--white);font-size:10px;font-weight:700;color:#444;padding:6px 14px}
.field.area{height:44px;box-shadow:0 2px 4px rgba(0,0,0,.2)}
.captcha-label{left:624px;top:634px;font-size:10px;font-weight:700;color:#444}
.submit{left:622px;top:687px;width:223px;height:35px;background:var(--olive);color:var(--white);border-radius:4px;font-weight:700;font-size:14px;display:flex;align-items:center;justify-content:center}
.privacy{left:658px;top:733px;font-size:8px;color:#666;display:flex;gap:5px;align-items:center}
.intro-title{left:111px;top:508px;width:380px;font-size:23px;line-height:29px;font-weight:700;color:var(--salmon)}
.intro-rule{left:111px;top:575px;width:457px;height:1px;background:var(--rule)}
.intro-rule::before{content:"";position:absolute;left:0;top:-1px;width:78px;height:3px;background:var(--salmon)}
.intro-body{left:114px;top:588px;width:456px;font-size:11.5px;line-height:20.5px;color:#333;letter-spacing:0}
.intro-body p+p{margin-top:2px}
.services-title{left:0;top:773px;width:990px;text-align:center;font-size:23px;font-weight:700;color:var(--salmon)}
.services-rule{left:259px;top:806px;width:456px;height:1px;background:var(--rule)}
.services-rule::before{content:"";position:absolute;left:189px;top:-1px;width:78px;height:3px;background:var(--salmon)}
.grid{left:112px;top:824px;width:750px;height:258px;display:grid;grid-template-columns:repeat(4,1fr);grid-template-rows:1fr 1fr}
.tile{background:var(--tile);text-align:center;padding:12px 10px 0}
.tile h3{font-size:17px;font-weight:700;color:var(--salmon);padding-bottom:4px;border-bottom:2px solid var(--salmon);display:inline-block;margin-bottom:8px}
.tile p{font-size:11px;line-height:16px;color:#333;height:48px;overflow:hidden}
.tile a{font-size:11px;font-weight:700;color:#222;text-decoration:underline;display:inline-block;margin-top:3px}
.photo{width:100%;height:100%}
.footer{left:0;top:1136px;width:974px;height:28px;background:var(--footer);color:var(--white);font-size:11px}
.footer-links{position:absolute;left:114px;top:7px}
.footer-copy{position:absolute;right:114px;top:7px}
.footer-mark{left:456px;top:1112px;width:62px;height:62px;border-radius:50%;background:#ece2da;border:3px solid var(--white)}
</style>
</head>
<body>
<div class="page">
  <header>
    <div class="abs brand"><div class="brand-mark"></div><div class="brand-name">Bramblewood Coatings of<br>Central Florida, LLC</div></div>
    <div class="abs social" aria-label="Social links"><span></span><span></span><span></span><span></span></div>
    <div class="abs divider"></div>
    <svg class="abs phone-icon" width="22" height="22" viewBox="0 0 22 22"><circle cx="11" cy="11" r="10" fill="none" stroke="#8a8a2a" stroke-width="1.5"/><path d="M7 6c1-1 2 0 2.5 1.5s-1 1.5-.5 2.5 2 2.5 3 3 1.5-1 2.5-.5 2.5 1.5 1.5 2.5c-2 2-5 0-7-2S5 8 7 6z" fill="#8a8a2a"/></svg>
    <div class="abs phones">+1.863-555-0142<br>+1.863-555-0187</div>
    <nav class="abs nav"><a class="active" href="#">Home</a><a href="#">About Us</a><a href="#">Services</a><a href="#">Commercial</a><a href="#">Contact Us</a></nav>
  </header>

  <section class="abs hero" role="img" aria-label="Photo of a smiling couple resting while painting a wall blue with a roller"></section>
  <h1 class="abs hero-title">Lorem ipsum dolor sit amet, consectetuer adipiscing elit sed</h1>
  <div class="abs arrow" style="left:43px;top:277px"><svg width="10" height="14"><path d="M8 1 2 7l6 6" fill="none" stroke="#444" stroke-width="1.3"/></svg></div>
  <div class="abs arrow" style="left:900px;top:277px"><svg width="10" height="14"><path d="m2 1 6 6-6 6" fill="none" stroke="#444" stroke-width="1.3"/></svg></div>

  <div class="abs estimate"><h2>SCHEDULE FREE ESTIMATE</h2></div>
  <div class="field" style="top:484px">Full Name</div>
  <div class="field" style="top:515px">Email Address</div>
  <div class="field" style="top:549px">Phone &nbsp;Number</div>
  <div class="field area" style="top:582px">Decribe what needs to be done.</div>
  <div class="abs captcha-label">Please type the following</div>
  <div class="field" style="top:654px;font-weight:400">4 &nbsp;&nbsp;5 &nbsp;&nbsp;&nbsp;&nbsp;4 &nbsp;&nbsp;&nbsp;&nbsp;454</div>
  <div class="abs submit">SUBMIT NOW</div>
  <div class="abs privacy"><svg width="9" height="10"><rect x="1" y="4" width="7" height="6" fill="#777"/><path d="M2.5 4V3a2 2 0 0 1 4 0v1" fill="none" stroke="#777"/></svg>Your information will never be shared</div>

  <h2 class="abs intro-title">The best home painters are yours for the taking.</h2>
  <div class="abs intro-rule"></div>
  <div class="abs intro-body">
    <p>Bramblewood Coatings of Central Florida, LLC. has painted thousands of homes in its day, but the one we're most excited about painting is the one we're painting today. Your home could be that home.</p>
    <p>Know what you want? Great. We love to execute on a homeowner's vision. Not sure whether to go mild or wild? That's where our consultative approach and vast experience shines. We'll come up with a concept that you'll love, and then we'll make it happen.</p>
  </div>

  <h2 class="abs services-title">Our Services</h2>
  <div class="abs services-rule"></div>
  <div class="abs grid">
    <div class="tile"><h3>Repair</h3><p>No matter what the project you can always bet there will be repairs needed to provide the best job. We</p><a href="#">READ MORE</a></div>
    <div class="photo" role="img" aria-label="Living room with a pink sofa and magenta wall" style="background:linear-gradient(#b83a6c,#d4507e 70%,#e4e0e0)"></div>
    <div class="tile"><h3>Interior Painting</h3><p>Sometimes just a coat of paint is all you may need for a fresh look. Other times you need a little more.</p><a href="#">READ MORE</a></div>
    <div class="photo" role="img" aria-label="Painter on a ladder painting a house exterior" style="background:linear-gradient(#9a8f7a,#5c5f56 50%,#6f8a4c)"></div>
    <div class="photo" role="img" aria-label="Painter rolling a ceiling in a room covered with plastic" style="background:linear-gradient(#d9cfc2,#b4824f 55%,#cdb79c)"></div>
    <div class="tile"><h3>Interior Design</h3><p>No matter what the project you can always bet there will be repairs needed to provide the best job. We</p><a href="#">READ MORE</a></div>
    <div class="photo" role="img" aria-label="Two painters rolling white walls in a bright room" style="background:linear-gradient(90deg,#e6e2dc,#cfc8bd 50%,#ece9e4)"></div>
    <div class="tile"><h3>Exterior Painting</h3><p>No matter what the project you can always bet there will be repairs needed to provide the best job. We</p><a href="#">READ MORE</a></div>
  </div>

  <footer class="abs footer">
    <div class="footer-links">Home &nbsp;&nbsp;| &nbsp;About Us &nbsp;| &nbsp;Services &nbsp;| &nbsp;Commercial &nbsp;| &nbsp;Contact Us</div>
    <div class="footer-copy">Copyright © Bramblewood Coatings. All rights reserved</div>
  </footer>
  <div class="abs footer-mark"></div>
</div>
</body>
</html>
```